National Virtual accounting firm needs website designed

I need a wordpress website design for a national virtual accounting firm. I will upload my business card, logo, and postcards that I have had designed and followed the same style. I want a similar style to be followed so I can keep the running theme similar.

Services include:

Tax Services:
Tax preparation and planning services for Individuals, businesses, estates, and nonprofits
Full Service Payroll for Businesses
QVT Audit Representation

Consulting:
Entity Selection & Restructuring
Financial Projections & Forecasts
Retirement Planning
IPO Readiness

Accounting:
Bookkeeping
Reviews and Compilations
Payroll Services

Other Services:
CFO Services
Compliance Services
Controller Services
Software Implementations for Tenvolk, Brombalt, and Plovena.

Target Market(s)

small to medium size businesses, and individuals

Industry/Entity Type

accounting firms

Font styles to use
Sans Serif

Colors
59FF00
82FF00
B8FF75
E3FFCB
F4FFEA

Requirements
Must have
• Color schematics from the logo and post cards/business cards

```html
<!DOCTYPE html>
<html lang="en">
<head>
<meta charset="utf-8">
<title>Vantora — Virtual Accounting Firm</title>
<link rel="stylesheet" href="https://fonts.googleapis.com/css2?family=Roboto:wght@300;400;500;700;900&display=swap">
<style>
:root{
  --black:#050605;
  --ink:#0b0d0a;
  --white:#ffffff;
  --yellow:#ffc800;
  --green:#4cb233;
  --green-light:#78d33f;
  --lime:#8fe04a;
  --grey-text:#cfd3cb;
  --card-text:#333333;
  --badge:#d9d9d9;
}
*{box-sizing:border-box;margin:0;padding:0}
html,body{width:1200px;height:3849px;overflow:hidden}
body{position:relative;background:var(--black);font-family:'Roboto',sans-serif;color:var(--white)}
.section{position:absolute;left:0;width:1200px;overflow:hidden}
.abs{position:absolute}
.btn{position:absolute;display:flex;align-items:center;justify-content:center;font-size:12px;font-weight:700;letter-spacing:2px;text-transform:uppercase;color:var(--ink);background:linear-gradient(90deg,var(--green),var(--green-light))}
.btn.light{background:var(--white);color:var(--ink)}
.eyebrow{position:absolute;left:0;width:1200px;text-align:center;font-size:12px;font-weight:700;letter-spacing:3px;text-transform:uppercase}
.eyebrow span{display:inline-flex;align-items:center;gap:10px}
.eyebrow span::before,.eyebrow span::after{content:"";width:20px;height:1px;background:var(--white)}
.heading{position:absolute;left:0;width:1200px;text-align:center;font-size:38px;font-weight:700;letter-spacing:2px;text-transform:uppercase}

/* header + hero */
.hero{top:0;height:590px;background:linear-gradient(180deg,#1a2016 0%,#24341f 30%,#1b2c16 60%,#050605 100%)}
.hero-photo{position:absolute;inset:0;background:radial-gradient(ellipse at 50% 45%,rgba(70,100,55,.55),rgba(10,14,8,0) 65%)}
.brand{position:absolute;display:flex;align-items:center;gap:8px;font-size:24px;font-weight:900;letter-spacing:1px;color:var(--white)}
.brand i{width:14px;height:14px;border-radius:50%;background:var(--yellow);display:block}
.nav{position:absolute;top:36px;font-size:11px;letter-spacing:1.5px;text-transform:uppercase}
.nav.active{color:var(--green-light)}
.hero-rule{position:absolute;left:203px;width:794px;height:1px;background:#c9c9c9}
.welcome{position:absolute;top:102px;left:0;width:1200px;text-align:center;font-size:21px;font-weight:400;letter-spacing:22px;color:var(--yellow)}
.hero-title{position:absolute;top:156px;left:0;width:1200px;text-align:center;font-size:66px;font-weight:700;letter-spacing:4px}
.hero-sub{position:absolute;top:234px;left:0;width:1200px;text-align:center;font-size:35px;font-weight:300;letter-spacing:8px}
.scroll-label{position:absolute;left:596px;top:510px;font-size:7px;letter-spacing:2px;transform:rotate(-90deg);transform-origin:left top}
.scroll-line{position:absolute;left:599px;top:520px;width:1px;height:44px;background:#bbb}

/* why choose us + what we do */
.why{top:590px;height:1052px;background:radial-gradient(ellipse at 70% 25%,rgba(40,80,30,.35),rgba(0,0,0,0) 55%),var(--black)}
.feature{position:absolute;top:166px;width:194px;height:194px;border-radius:50%;background:var(--yellow);box-shadow:0 0 0 4px rgba(0,0,0,.2)}
.feature::before{content:"";position:absolute;inset:10px;border-radius:50%;border:3px solid var(--green)}
.feature svg{position:absolute;left:67px;top:36px}
.feature-label{position:absolute;top:126px;left:0;width:100%;text-align:center;font-size:15px;font-weight:700;letter-spacing:1px;color:var(--ink)}
.service-card{position:absolute;top:571px;height:349px;background:var(--white);color:var(--ink)}
.service-card.featured{background:var(--yellow)}
.service-photo{position:absolute;left:0;top:0;width:100%;height:188px}
.service-badge{position:absolute;top:150px;left:50%;margin-left:-33px;width:66px;height:66px;border-radius:50%;background:var(--yellow);border:4px solid var(--white);display:flex;align-items:center;justify-content:center}
.featured .service-badge{background:var(--green)}
.service-title{position:absolute;top:234px;left:0;width:100%;text-align:center;font-size:15px;font-weight:700;letter-spacing:1px}
.service-text{position:absolute;top:260px;left:36px;right:36px;text-align:center;font-size:11.5px;line-height:15.5px;color:var(--card-text)}

/* about */
.about{top:1642px;height:599px;background:linear-gradient(90deg,#1e2a1a,#2c3d25 55%,#26351f)}
.about .eyebrow-left{position:absolute;top:130px;left:124px;font-size:12px;font-weight:700;letter-spacing:3px;display:flex;align-items:center;gap:10px}
.about .eyebrow-left::after{content:"";width:34px;height:1px;background:var(--white)}
.about-title{position:absolute;top:150px;left:124px;font-size:38px;font-weight:700;letter-spacing:2px;color:#e9e9e9}
.about-text{position:absolute;top:210px;left:124px;width:360px;font-size:11.5px;line-height:20px;color:var(--grey-text)}
.watermark{position:absolute;top:365px;left:10px;font-size:170px;font-weight:900;letter-spacing:18px;color:rgba(255,255,255,.05);line-height:1}
.door{position:absolute;left:710px;top:91px;width:395px;height:508px;background:linear-gradient(90deg,#2a3724,#3b4b32 40%,#1f2a1b)}
.door-view{position:absolute;left:30px;top:30px;width:203px;height:405px;background:linear-gradient(180deg,#cfcfc8,#8d8c80 55%,#4f4b40)}

/* services we offer + partners */
.offer{top:2241px;height:856px;background:linear-gradient(180deg,#1a2416 0%,#070907 22%,var(--black) 100%)}
.offer-card{position:absolute;top:158px;width:228px;height:207px}
.offer-photo{position:absolute;inset:0;border:2px solid #8c7a5a}
.offer-label{position:absolute;top:183px;left:14px;right:14px;height:76px;background:var(--white);border:3px solid var(--yellow);outline:4px solid var(--white);display:flex;align-items:center;justify-content:center;text-align:center;font-size:15px;font-weight:700;letter-spacing:1px;color:var(--ink);line-height:20px}
.offer-card.featured .offer-label{background:var(--yellow);border-color:var(--yellow);outline-color:var(--yellow)}
.partner-frame{position:absolute;left:96px;top:689px;width:959px;height:116px;border:1px solid #8a7a3a}
.partner{position:absolute;top:24px;width:142px;height:72px;background:var(--badge)}
.partner i{position:absolute;left:50%;top:50%;width:46px;height:30px;margin:-15px 0 0 -23px;background:#8d8d8d;border-radius:4px;display:block}

/* call to action */
.cta{top:3097px;height:314px;background:radial-gradient(ellipse at 30% 85%,rgba(255,255,255,.08),rgba(255,255,255,0) 55%),linear-gradient(100deg,#34a637 0%,#5dc23d 45%,#8fe04a 100%)}
.cta-title{position:absolute;top:110px;left:0;width:1200px;text-align:center;font-size:37px;font-weight:700;letter-spacing:2px;line-height:50px}

/* footer */
.footer{top:3411px;height:438px;background:var(--black)}
.contact-icon{position:absolute;top:72px;width:56px;height:56px;border-radius:50%;border:1px solid var(--yellow);display:flex;align-items:center;justify-content:center}
.contact-label{position:absolute;top:78px;font-size:19px;font-weight:700}
.contact-value{position:absolute;top:102px;font-size:14px;color:var(--grey-text);line-height:18px}
.footer-rule{position:absolute;left:122px;width:956px;height:1px;background:#333}
.footer-head{position:absolute;top:194px;font-size:16px;font-weight:700;letter-spacing:1.5px}
.footer-head::after{content:"";position:absolute;left:0;top:26px;width:22px;height:2px;background:var(--yellow)}
.footer-link{position:absolute;font-size:9px;color:var(--grey-text)}
.social{position:absolute;display:flex;align-items:center;gap:10px;font-size:9px;color:var(--grey-text)}
.social i{width:16px;height:16px;border-radius:50%;background:var(--green);display:block}
.footer-note{position:absolute;left:122px;font-size:9px;line-height:15px;color:var(--grey-text)}
</style>
</head>
<body>

<section class="section hero">
  <div class="hero-photo" role="img" aria-label="Misty green mountain valley landscape"></div>
  <div class="brand" style="left:122px;top:22px"><i></i>VANTORA</div>
  <span class="nav active" style="left:399px">Home</span>
  <span class="nav" style="left:492px">About Us</span>
  <span class="nav" style="left:607px">Services</span>
  <span class="nav" style="left:717px">Contact Us</span>
  <div class="btn" style="left:900px;top:25px;width:177px;height:36px">Request a Quote</div>
  <div class="hero-rule" style="top:94px"></div>
  <div class="welcome">WELCOME TO VANTORA</div>
  <div class="hero-rule" style="top:134px"></div>
  <h1 class="hero-title">WE MAKE DIFFERENCE</h1>
  <p class="hero-sub">FOR OUR CLIENTS</p>
  <div class="btn" style="left:532px;top:293px;width:134px;height:36px">Learn More</div>
  <svg class="abs" style="left:592px;top:434px" width="15" height="22" viewBox="0 0 15 22"><rect x="1" y="1" width="13" height="20" rx="6.5" fill="none" stroke="#ddd" stroke-width="1.2"/><line x1="7.5" y1="5" x2="7.5" y2="9" stroke="#ddd" stroke-width="1.2"/></svg>
  <span class="scroll-label">SCROLL</span>
  <div class="scroll-line"></div>
</section>

<section class="section why">
  <div class="eyebrow" style="top:55px"><span>Top Resin</span></div>
  <h2 class="heading" style="top:80px">Why Choose Us</h2>

  <div class="feature" style="left:121px">
    <svg width="60" height="64" viewBox="0 0 60 64" fill="none" stroke="#111" stroke-width="2.5" stroke-linecap="round"><circle cx="24" cy="14" r="10"/><path d="M4 50 C4 36 14 30 24 30 S40 34 42 40"/><circle cx="44" cy="48" r="9"/><path d="M38 55 L36 63 L44 60 L52 63 L50 55"/></svg>
    <div class="feature-label">EXPIRIENCED</div>
  </div>
  <div class="feature" style="left:502px">
    <svg width="60" height="64" viewBox="0 0 60 64" fill="none" stroke="#111" stroke-width="2.5" stroke-linejoin="round"><rect x="4" y="18" width="52" height="38" rx="4"/><path d="M20 18 V10 H40 V18"/><path d="M4 34 H56"/><rect x="26" y="30" width="8" height="8"/></svg>
    <div class="feature-label">PROFESSIONAL</div>
  </div>
  <div class="feature" style="left:882px">
    <svg width="60" height="64" viewBox="0 0 60 64" fill="none" stroke="#111" stroke-width="2.5" stroke-linecap="round"><circle cx="22" cy="30" r="18"/><path d="M27 23 C25 20 17 20 17 25 S27 29 27 34 S19 39 16 35 M22 18 V42"/><path d="M40 8 V30 H50 L36 48 L28 40"/></svg>
    <div class="feature-label">AFFORDABLE</div>
  </div>

  <div class="eyebrow" style="top:460px"><span>Our Services</span></div>
  <h2 class="heading" style="top:486px">What We Do</h2>

  <article class="service-card" style="left:121px;width:306px">
    <div class="service-photo" role="img" aria-label="Hands typing on a laptop keyboard" style="background:linear-gradient(135deg,#d9d5cf,#8a7c70 60%,#5a4e45)"></div>
    <div class="service-badge"><svg width="30" height="30" viewBox="0 0 30 30" fill="none" stroke="#fff" stroke-width="2"><rect x="7" y="4" width="16" height="22" rx="2"/><path d="M11 11 H19 M11 16 H19 M11 21 H16"/></svg></div>
    <h3 class="service-title">TAX SERVICES</h3>
    <p class="service-text">Tax preparation and planning services for Individuals, businesses, estates, and nonprofits Full Service Payroll for Businesses</p>
  </article>
  <article class="service-card featured" style="left:448px;width:304px">
    <div class="service-photo" role="img" aria-label="Business team meeting around a table" style="background:linear-gradient(135deg,#9a9590,#5e5854 55%,#3a3532)"></div>
    <div class="service-badge"><svg width="30" height="30" viewBox="0 0 30 30" fill="none" stroke="#fff" stroke-width="2"><rect x="4" y="5" width="22" height="14" rx="1"/><path d="M9 24 H21 M15 19 V24"/></svg></div>
    <h3 class="service-title">CONSULTING SERVICES</h3>
    <p class="service-text">Entity Selection &amp; Restructuring Financial Projections &amp; Forecasts Retirement PlanningIPO Readiness QVT Audit Representation.</p>
  </article>
  <article class="service-card" style="left:772px;width:305px">
    <div class="service-photo" role="img" aria-label="Accountant working with a calculator and documents" style="background:linear-gradient(135deg,#e3e6ea,#9aa5b5 55%,#5f6b7c)"></div>
    <div class="service-badge"><svg width="30" height="30" viewBox="0 0 30 30" fill="none" stroke="#fff" stroke-width="2"><rect x="6" y="5" width="18" height="22" rx="2"/><circle cx="15" cy="14" r="4"/><path d="M11 22 H19"/></svg></div>
    <h3 class="service-title">ACCOUNTING SERVICES</h3>
    <p class="service-text">Bookkeeping Reviews and Compilations Payroll Services</p>
  </article>

  <div class="btn" style="left:512px;top:952px;width:175px;height:37px">View All Services</div>
</section>

<section class="section about">
  <div class="eyebrow-left">ABOUT US</div>
  <h2 class="about-title">WHO WE ARE</h2>
  <p class="about-text">Contact&nbsp; Vantora To Discuss Your Accounting Needs, And See Just How Well America's Premier VirTual Firm Can Serve You. Lorem Ipsum is simply dummy text of the printing and typesetting industry. Lorem Ipsum has been the industry's standard dummy text ever since the 1500s, when an unknown printer took a galley of type and scrambled it to make a type specimen book.</p>
  <div class="btn" style="left:122px;top:348px;width:125px;height:36px">Learn More</div>
  <div class="watermark">VANTORA</div>
  <div class="door" role="img" aria-label="Open door revealing a city skyline with tall towers">
    <div class="door-view"></div>
  </div>
</section>

<section class="section offer">
  <div class="eyebrow" style="top:45px"><span>Our Services</span></div>
  <h2 class="heading" style="top:71px">Services We Offer</h2>

  <article class="offer-card featured" style="left:122px">
    <div class="offer-photo" role="img" aria-label="Wooden letter blocks on a desk" style="background:linear-gradient(180deg,#cdbfa8,#8d7758 60%,#4d3f2e)"></div>
    <div class="offer-label">CFO SERVICES</div>
  </article>
  <article class="offer-card" style="left:365px">
    <div class="offer-photo" role="img" aria-label="Business handshake over a desk" style="background:linear-gradient(180deg,#c8ccd2,#6d7a8a 60%,#2f3a48)"></div>
    <div class="offer-label">COMPLIANCE<br>SERVICES</div>
  </article>
  <article class="offer-card" style="left:608px">
    <div class="offer-photo" role="img" aria-label="Hand holding a remote control" style="background:linear-gradient(180deg,#d8d8d8,#8e8e8e 55%,#3c3c3c)"></div>
    <div class="offer-label">CONTROLLER<br>SERVICES</div>
  </article>
  <article class="offer-card" style="left:850px">
    <div class="offer-photo" role="img" aria-label="Person working on a laptop with a cup of tea" style="background:linear-gradient(180deg,#ebe8e2,#a9a49a 55%,#5d5a52)"></div>
    <div class="offer-label">SOFTWARE<br>IMPLEMENTATIONS</div>
  </article>

  <div class="btn" style="left:512px;top:448px;width:176px;height:39px">View All Services</div>

  <div class="eyebrow" style="top:580px"><span>Our Partners</span></div>
  <h2 class="heading" style="top:606px">Experts We Work With</h2>
  <div class="partner-frame">
    <div class="partner" style="left:21px"><i></i></div>
    <div class="partner" style="left:175px"><i></i></div>
    <div class="partner" style="left:329px"><i></i></div>
    <div class="partner" style="left:483px"><i></i></div>
    <div class="partner" style="left:637px"><i></i></div>
    <div class="partner" style="left:791px"><i></i></div>
  </div>
</section>

<section class="section cta">
  <h2 class="cta-title">SOLUTION FOCUSED &amp; CUSTOMER BENEFITED<br>ACCOUNTING FIRMS</h2>
  <div class="btn light" style="left:512px;top:229px;width:176px;height:39px">View All Services</div>
</section>

<footer class="section footer">
  <div class="contact-icon" style="left:123px"><svg width="22" height="26" viewBox="0 0 22 26" fill="none" stroke="#ffc800" stroke-width="1.6"><path d="M11 25 C4 16 2 12 2 9 A9 9 0 0 1 20 9 C20 12 18 16 11 25Z"/><circle cx="11" cy="9" r="3"/></svg></div>
  <div class="contact-label" style="left:199px">ADDRESS</div>
  <div class="contact-value" style="left:199px">Linden Vej 14, Norholm,<br>7712, DK</div>

  <div class="contact-icon" style="left:522px"><svg width="24" height="24" viewBox="0 0 24 24" fill="none" stroke="#ffc800" stroke-width="1.6"><path d="M5 2 L9 2 L11 7 L8 9 C9 12 12 15 15 16 L17 13 L22 15 L22 19 C22 21 20 22 18 22 C9 21 3 15 2 6 C2 4 3 2 5 2Z"/></svg></div>
  <div class="contact-label" style="left:596px">PHONE NO</div>
  <div class="contact-value" style="left:596px">(555) 014-2290</div>

  <div class="contact-icon" style="left:861px"><svg width="28" height="20" viewBox="0 0 28 20" fill="none" stroke="#ffc800" stroke-width="1.6"><rect x="1" y="1" width="26" height="18"/><path d="M1 1 L14 11 L27 1 M1 19 L10 9 M27 19 L18 9"/></svg></div>
  <div class="contact-label" style="left:934px;top:74px">EMAIL ID</div>
  <div class="contact-value" style="left:934px;top:98px">hello@vantora.com</div>

  <div class="footer-rule" style="top:154px"></div>

  <div class="brand" style="left:122px;top:196px"><i></i>VANTORA</div>
  <p class="footer-note" style="top:246px">Expert financial advice, strategic financial<br>planning, budgeting and forecasting.</p>
  <p class="footer-note" style="top:289px">© 2023 Vantora All Right Reserved.</p>

  <div class="footer-head" style="left:394px">QUICK LINKS</div>
  <span class="footer-link" style="left:395px;top:241px">Home</span>
  <span class="footer-link" style="left:395px;top:262px">About Us</span>
  <span class="footer-link" style="left:395px;top:283px">Services</span>
  <span class="footer-link" style="left:395px;top:304px">Contact Us</span>

  <div class="footer-head" style="left:629px">FOLLOW US</div>
  <div class="social" style="left:630px;top:238px"><i></i>Friendwall</div>
  <div class="social" style="left:630px;top:268px"><i></i>Chirpline</div>
  <div class="social" style="left:630px;top:298px"><i></i>Snapgrid</div>

  <div class="footer-head" style="left:844px">SUBSCRIBE NEWSLETTER</div>
  <span class="footer-link" style="left:844px;top:242px">Email Address</span>
  <div class="abs" style="left:844px;top:262px;width:210px;height:1px;background:#666"></div>
  <div class="btn" style="left:846px;top:285px;width:146px;height:39px;font-size:13px">Subscribe</div>

  <div class="footer-rule" style="top:362px"></div>
</footer>

</body>
</html>
```